Zielgruppe
wir sind eine Sicherheitsunternehmen und suchen ein ausgefallenes Design um alle Privathaushalte sowohl auch kleine und große Firmen zu beindrucken.
Aufgabenstellung
Die Firma möchte das erste Sicherheitsunternehmen sein was absolut Nachhaltig, ökologisch und umweltfreundlich arbeitet. Die Natur, der Klimawechsel steht im absoluten Vordergrund. Wir möchten zeigen das man auch als Dienstleister im Sicheheitsbereich im Einklang mit der Umwelt sein kann. und mit diesem Konzept möchten wir an die Bevölkerung rantreten. Das Motto: mit uns als Partner werden Fremdfirmen mehr Kunden gewinnen, da wir umweltbewusst und mit den uns verfügbaren Ressourcen sehr ökologisch und grün sind. Das Design sollte bitte nicht in schrillen Farben dargestellt werden. Das Logo und unsere Grundfarben sind Schwarz/ Antrazith/ Weiss/Creme und Naturrholzfarben.

```html
<!DOCTYPE html>
<html lang="de">
<head>
<meta charset="utf-8">
<title>Solvia Sicherheit – Faltblatt</title>
<link href="https://fonts.googleapis.com/css2?family=Arimo:wght@400;700&family=Alfa+Slab+One&display=swap" rel="stylesheet">
<style>
  :root {
    --page: #ffffff;
    --ink: #141414;
    --ink-soft: #222222;
    --cream: #f1ddb0;
    --night-text: #e6ecf3;
    --night-accent: #e4ecf7;
    --brand-grey: #8e97a4;
    --olive: #3b3409;
    --white: #ffffff;
    --badge: #0c0c0c;
  }
  * { margin: 0; padding: 0; box-sizing: border-box; }
  html, body { width: 1200px; height: 574px; overflow: hidden; background: var(--page); }
  body { position: relative; font-family: "Arimo", Arial, sans-serif; }

  .panel { position: absolute; top: 0; height: 574px; overflow: hidden; }
  .panel-cover { left: 2px; width: 286px; }
  .panel-inside { left: 311px; width: 575px; }
  .panel-contact { left: 912px; width: 286px; }

  .panel-bg { position: absolute; inset: 0; }
  .panel-cover .panel-bg {
    background: linear-gradient(180deg, #d3e0f3 0%, #e3ebf4 30%, #dbe6f0 48%, #9bb1cf 62%, #8ea6c8 70%, #d9c9a0 82%, #b9c45a 92%, #9aae3a 100%);
  }
  .panel-inside .panel-bg {
    background: radial-gradient(ellipse 45% 60% at 70% 40%, #2a5a8c 0%, #183b60 45%, transparent 80%),
                linear-gradient(180deg, #0d2338 0%, #123050 50%, #0b1b2d 100%);
  }
  .panel-contact .panel-bg {
    background: linear-gradient(180deg, #fbfbf8 0%, #f4f2e6 35%, #e3da9a 48%, #c9b646 58%, #8b7f24 70%, #5e5c1c 84%, #4a4b1a 100%);
  }

  .centered { position: absolute; text-align: center; }

  /* Cover */
  .cover-headline { top: 15px; left: 0; width: 100%; font-weight: 700; font-size: 24px; line-height: 30.7px; color: var(--ink); }
  .cover-values { top: 104px; left: 0; width: 100%; font-size: 18px; line-height: 23px; color: var(--ink); }
  .cover-claim { top: 197px; left: 0; width: 100%; font-size: 19px; line-height: 23px; color: var(--ink); }
  .cover-badge {
    position: absolute; left: 6px; top: 336px; width: 280px; height: 34px;
    background: var(--badge); border: 2px solid var(--white); border-radius: 5px;
    transform: rotate(-9deg); display: flex; align-items: center; justify-content: center;
    font-family: "Alfa Slab One", Georgia, serif; font-size: 16px; color: var(--white); white-space: nowrap;
  }
  .brand-name { position: absolute; left: 0; width: 100%; text-align: center; font-weight: 700; text-transform: uppercase; letter-spacing: 1.2px; }
  .panel-cover .brand-name { top: 552px; font-size: 9.5px; color: var(--white); }

  /* Inside */
  .col { position: absolute; width: 240px; text-align: center; }
  .col-left { left: 25px; top: 31px; }
  .col-right { left: 316px; top: 33px; }
  .col h2 { font-size: 15.5px; line-height: 19.3px; font-weight: 700; color: var(--cream); }
  .col-right h2 { line-height: 17.4px; }
  .col h3 { font-size: 13.5px; line-height: 15.4px; font-weight: 700; color: var(--night-text); margin-top: 20px; }
  .col p { font-size: 12.8px; line-height: 15.4px; color: var(--night-text); }
  .col .gap { margin-top: 15px; }
  .services-title { font-size: 16px; line-height: 18px; font-weight: 700; color: var(--cream); margin-top: 41px; }
  .service { font-size: 12.8px; line-height: 13.5px; color: var(--night-text); margin-top: 5px; }
  .service:first-of-type { margin-top: 0; }
  .service b { color: var(--night-accent); font-size: 13.2px; }
  .services-note { margin-top: 6px; font-size: 12.8px; line-height: 15.4px; color: var(--night-text); }
  .services-cta { margin-top: 6px; font-size: 15.5px; line-height: 15.5px; font-weight: 700; color: var(--cream); }
  .panel-inside .brand-name { top: 526px; font-size: 12.5px; letter-spacing: 2px; color: var(--brand-grey); }

  /* Contact */
  .contact-text { left: 12px; top: 19px; width: 262px; }
  .contact-text h2 { font-size: 16px; line-height: 17.5px; font-weight: 700; color: var(--ink); margin-bottom: 4px; }
  .contact-text p { font-size: 12.6px; line-height: 15.4px; color: var(--ink-soft); margin-top: 7px; }
  .contact-text p:first-of-type { margin-top: 6px; }
  .contact-cta { font-size: 15.5px; line-height: 19px; font-weight: 700; color: var(--olive); margin-top: 4px; }
  .panel-contact .brand-name { top: 500px; font-size: 9px; color: var(--white); }
  .contact-address { top: 513px; left: 0; width: 100%; font-size: 9.5px; line-height: 11.6px; color: var(--white); }
</style>
</head>
<body>

<section class="panel panel-cover">
  <div class="panel-bg" role="img" aria-label="Foto: Hand hält die Erdkugel vor hellem Himmel und sonniger Wiese"></div>
  <h1 class="centered cover-headline">Wenn es darauf<br>ankommt, bewachen<br>wir die ganze Welt...</h1>
  <p class="centered cover-values">...ökologisch<br>nachhaltig<br>umweltfreundlich</p>
  <p class="centered cover-claim">Sicherheit, die sich jeder<br>leisten kann</p>
  <div class="cover-badge">...so gewinnen Sie neue Kunden</div>
  <div class="brand-name">Solvia Sicherheit Mirabell Huter</div>
</section>

<section class="panel panel-inside">
  <div class="panel-bg" role="img" aria-label="Foto: Sicherheitsmitarbeiter mit Taschenlampe in nächtlichem Blau"></div>

  <div class="col col-left">
    <h2>Wir sind eins der ersten Sicherheitsunternehmen, die nachhaltig, ökologisch und umweltfreundlich arbeiten.</h2>
    <h3>Was heißt das?</h3>
    <p>Wir sind ein zu 95% ökologischer Betrieb. Unsere Dienstfahrzeuge sind ausschließlich Hybridfahrzeuge. Die Dientskleidung wird so weit wie möglich ökologisch und ohne Kinder­arbeit hergestellt. Unsere Betriebs­räume werden mit 100%-Ökostrom betrieben. Inneneinrichtungen sowie Büromaterial sind aus recyclebaren Rohstoffen.</p>
    <p class="gap" style="margin-top:32px">Sicherheit heißt frei von Angst und Gefahr zu sein. Mit steigender Kri­minalität steigt das Bedürfniss nach Sicherheit. Wir bieten alle erfoder­lichen Voraussetzungen zur Siche­rung von Personen, Gebäuden, Einrichtungen und Sachwerten. Dazu übernehmen wir aber auch Urlaubsvertretungen wie Versorgung von Tieren oder Pflanzen.</p>
  </div>

  <div class="col col-right">
    <h2>Sicherheit für Familien, Klein­betriebe, Firmen, Groß­objekte, Veranstaltungen usw.</h2>
    <div class="services-title">Das sind unsere Leistungen:</div>
    <div class="service"><b>Objektschutz</b> wie z.B.<br>Gebäudebewachung<br>Bühnenbewachung<br>Baustellenbewachung<br>Revierkontrollen<br>Außenkontrollen</div>
    <div class="service"><b>Werkschutz</b><br>Pfortendienste<br>Nachtdienste</div>
    <div class="service"><b>Veranstaltungsschutz</b></div>
    <div class="service"><b>Sicherheitstransporte</b><br>Dokumentenlieferung<br>Werttransporte</div>
    <div class="service"><b>Zugbegleitung</b><br>Fahrausweiskontrolle</div>
    <div class="service"><b>Personenschutz</b></div>
    <p class="services-note">Die Palette ist so groß, dass wir nur einen kleinen Teil aufzählen können. fragen Sie danach.</p>
    <div class="services-cta">Mit unserer Leistung<br>gewinnen Sie<br>neue Kunden!</div>
  </div>

  <div class="brand-name">Solvia Sicherheit Mirabell Huter</div>
</section>

<section class="panel panel-contact">
  <div class="panel-bg" role="img" aria-label="Foto: unscharfe sonnige Natur in Gelb- und Grüntönen"></div>
  <div class="centered contact-text">
    <h2>Sie wollen mehr über uns erfahren?</h2>
    <h2>Sie haben Fragen?</h2>
    <h2>Sie benötigen Beratung?</h2>
    <p>Für alle Ihre Fragen nehmen wir uns viel Zeit. Gern laden wir Sie zu ausführli­chen und kostenfreien Informations- und Beratungsgesprächen ein. Unser kompetentes, intensiv geschultes Team steht Ihnen jederzeit zur Verfügung.</p>
    <p>Wir sind Mitglied im BVWS und der BGSD, sowie Fördermitglied der Naturschutzinitiative Grünfeld.</p>
    <p>Demnächst bieten wir in unseren Räumen diverse Schulungen wie Ersthelfer, Brandschutz usw. an. Mehr darüber dann auf unserer Internetseite.</p>
    <div class="contact-cta">Vereinbaren Sie mit uns unter 04721-5839012 einen Termin</div>
  </div>
  <div class="brand-name">Solvia Sicherheit Mirabell Huter</div>
  <address class="centered contact-address" style="font-style:normal">
    Solvia Sicherheit Mirabell Huter<br>
    Wächterweg 12 - 54321 Grünfeld<br>
    04721-58390 - Mobil 0152-908172<br>
    info@solvia-schutz.de - www.solvia-schutz.de
  </address>
</section>

</body>
</html>
```